Business Card for TLK Field Services

Would like a large logo on one side. On the other side, logo on one side and company phone number, address, and email on the other side. I don't have a logo so please create one for us.
Updates
I don't have a logo, so please create one for us.
Target Market(s)
Land Surveying
Industry/Entity Type
Surveyor
Contact Information for Business Card
Would like a large logo on one side. On the other side, logo on one side and company phone number, address, and email on the other side
Requirements
Nice to have
- would like the initials to be incorporated with the logo

```html
<!DOCTYPE html>
<html lang="en">
<head>
<meta charset="utf-8">
<title>TLK Field Services – Business Card</title>
<link rel="stylesheet" href="https://fonts.googleapis.com/css2?family=Lato:wght@400;700;900&display=swap">
<style>
  :root {
    --backdrop: #3a3330;
    --brand-green: #76935f;
    --card-white: #ffffff;
    --ink: #1f1f1f;
    --band-dark: #262626;
    --rule-grey: #5a5a5a;
  }
  * { box-sizing: border-box; margin: 0; padding: 0; }
  html, body {
    width: 1200px; height: 900px; overflow: hidden;
    background: var(--backdrop);
    font-family: "Lato", sans-serif;
  }
  .stage { position: relative; width: 1200px; height: 900px; }

  .card {
    position: absolute;
    width: 620px; height: 354px;
    overflow: hidden;
  }

  /* Front face */
  .card-front {
    left: 60px; top: 60px;
    background: var(--brand-green);
    display: flex; align-items: center; justify-content: center;
  }
  .brand-lockup {
    display: flex; align-items: center; gap: 18px;
  }
  .brand-dot {
    width: 30px; height: 30px; border-radius: 50%;
  }
  .brand-name {
    font-weight: 900; text-transform: uppercase; letter-spacing: 1px;
    line-height: 1;
  }
  .card-front .brand-dot { background: var(--card-white); }
  .card-front .brand-name { color: var(--card-white); font-size: 40px; }

  /* Back face */
  .card-back {
    left: 520px; top: 486px;
    background: var(--card-white);
  }
  .card-back .brand-lockup {
    position: absolute; left: 34px; top: 92px; gap: 12px;
  }
  .card-back .brand-dot { background: var(--ink); width: 22px; height: 22px; }
  .card-back .brand-name { color: var(--ink); font-size: 26px; }

  .contact-block {
    position: absolute; left: 352px; top: 82px;
  }
  .person-name {
    color: var(--ink); font-weight: 700; font-size: 22px;
    letter-spacing: 6px; text-transform: uppercase;
  }
  .person-title {
    color: var(--brand-green); font-size: 15px;
    letter-spacing: 2.5px; text-transform: uppercase; margin-top: 4px;
  }
  .contact-list {
    list-style: none; margin-top: 16px;
    color: var(--ink); font-size: 13.5px; line-height: 1.55;
  }
  .contact-rule {
    position: absolute; left: 280px; right: 0; top: 238px;
    height: 2px; background: var(--rule-grey);
  }
  .address-band {
    position: absolute; left: 0; right: 0; top: 262px; height: 22px;
    background: var(--band-dark);
    color: var(--card-white); font-size: 12px;
    display: flex; align-items: center; padding-left: 150px;
  }
  .edge-bar {
    position: absolute; left: 380px; right: 0; bottom: 10px; height: 10px;
    background: var(--band-dark);
  }
</style>
</head>
<body>
<main class="stage">
  <section class="card card-front" aria-label="Business card front">
    <div class="brand-lockup">
      <span class="brand-dot"></span>
      <span class="brand-name">TLK Field Services</span>
    </div>
  </section>

  <section class="card card-back" aria-label="Business card back">
    <div class="brand-lockup">
      <span class="brand-dot"></span>
      <span class="brand-name">TLK Field<br>Services</span>
    </div>

    <div class="contact-block">
      <p class="person-name">Daniel Reed</p>
      <p class="person-title">Managing Director</p>
      <ul class="contact-list">
        <li>P: 555 0142 7788</li>
        <li>E: dan@tlkfield.com</li>
        <li>W: www.tlkfield.com</li>
      </ul>
    </div>

    <div class="contact-rule"></div>
    <div class="address-band">418 Ridge Road, Denver 80211</div>
    <div class="edge-bar"></div>
  </section>
</main>
</body>
</html>
```